Pheasant Farm needs a logo design

I need a logo design for my Pheasant farm. We raise Pheasants from chicks to adult birds for the hunting clubs dog training and restocking. I would like a logo that makes it easy to see that we deal with Pheasants. My company name is Larkin Meadow Pines located in northern MN. I'd like a pheasant in the logo if possible.

Target Market(s)

Hunting clubs, dog trainers, hunters

Contact Information for Business Card

Larkin Meadow Pines Dale Wexby cell 555-463-2098 office 555-302-7746 tallgrassfowlyard.com tallgrassfowlyard@quailpostmail.com
5816 Bramwell Rd NE
Fernvale, OR 97341

```html
<!DOCTYPE html>
<html lang="en">
<head>
<meta charset="utf-8">
<title>Larkin Meadow Pines – Business Card</title>
<link href="https://fonts.googleapis.com/css2?family=Questrial&display=swap" rel="stylesheet">
<style>
  :root {
    --backdrop: #2a2d31;
    --paper: #ffffff;
    --rust: #c9492f;
    --rust-light: #d9603f;
    --ink: #1c1f2e;
    --cream: #fbe3d9;
  }
  html, body {
    margin: 0;
    padding: 0;
    width: 1200px;
    height: 900px;
    overflow: hidden;
    background: var(--backdrop);
    font-family: "Questrial", "Century Gothic", sans-serif;
  }
  .canvas {
    position: relative;
    width: 1200px;
    height: 900px;
  }
  .card {
    position: absolute;
    left: 300px;
    width: 600px;
    height: 343px;
    background: var(--paper);
    overflow: hidden;
    box-shadow: 0 14px 30px rgba(0,0,0,.35);
  }
  .card--back { top: 70px; }
  .card--front { top: 487px; }

  /* Contact side */
  .card__split {
    position: absolute;
    inset: 0;
    width: 100%;
    height: 100%;
  }
  .brand {
    position: absolute;
    display: flex;
    align-items: center;
    gap: 10px;
    color: var(--rust);
    font-size: 19px;
    letter-spacing: .3px;
    white-space: nowrap;
  }
  .brand__dot {
    width: 22px;
    height: 22px;
    border: 2px solid var(--ink);
    border-radius: 50%;
    flex: none;
  }
  .card--back .brand { left: 22px; top: 156px; font-size: 16px; gap: 8px; }
  .card--back .brand__dot { width: 18px; height: 18px; }

  .contact {
    position: absolute;
    right: 30px;
    top: 42px;
    width: 290px;
    text-align: right;
    color: var(--paper);
  }
  .contact__company {
    margin: 0;
    font-size: 22px;
    font-weight: 400;
    letter-spacing: .5px;
    text-transform: uppercase;
    white-space: nowrap;
  }
  .contact__person {
    margin: 4px 0 0;
    font-size: 19px;
    color: var(--ink);
  }
  .contact__details {
    margin: 56px 0 0;
    padding: 0;
    list-style: none;
    font-size: 13.5px;
    line-height: 1.5;
    color: var(--cream);
    white-space: nowrap;
  }

  /* Logo side */
  .card__edge-top {
    position: absolute;
    left: 0; top: 0; right: 0;
    height: 10px;
    background: var(--rust);
  }
  .card__edge-right {
    position: absolute;
    top: 0; right: 0; bottom: 0;
    width: 10px;
    background: var(--rust);
  }
  .card__edge-left {
    position: absolute;
    top: 0; left: 0; bottom: 0;
    width: 3px;
    background: var(--ink);
  }
  .card--front .brand {
    left: 50%;
    top: 50%;
    transform: translate(-50%, -50%);
    font-size: 30px;
    gap: 14px;
  }
  .card--front .brand__dot { width: 30px; height: 30px; }
</style>
</head>
<body>
<main class="canvas">

  <section class="card card--back" aria-label="Business card, contact side">
    <svg class="card__split" viewBox="0 0 600 343" preserveAspectRatio="none" aria-hidden="true">
      <rect width="600" height="343" fill="var(--rust)"/>
      <path d="M330 0 H600 V343 H420 Z" fill="var(--rust-light)" opacity=".55"/>
      <path d="M0 0 H255 L262 280 Q264 304 240 310 L140 343 H0 Z" fill="var(--paper)"/>
    </svg>
    <div class="brand"><span class="brand__dot"></span>Larkin Meadow Pines</div>
    <div class="contact">
      <h1 class="contact__company">Larkin Meadow Pines</h1>
      <p class="contact__person">Dale Wexby</p>
      <ul class="contact__details">
        <li>555-463-2098</li>
        <li>555-302-7746</li>
        <li>tallgrassfowlyard.com</li>
        <li>tallgrassfowlyard@quailpostmail.com</li>
        <li>5816 Bramwell Rd NE Fernvale, OR 97341</li>
      </ul>
    </div>
  </section>

  <section class="card card--front" aria-label="Business card, logo side">
    <div class="card__edge-top"></div>
    <div class="card__edge-right"></div>
    <div class="card__edge-left"></div>
    <div class="brand"><span class="brand__dot"></span>Larkin Meadow Pines</div>
  </section>

</main>
</body>
</html>
```